Website design for a high-end equestrian business

Design a website to replace current one. Clean, simple, elegant design. I run a business training show jumping riders and horses, as well as buying and selling high quality horses. I run my business from a beautiful yard in Co. Kildare, Ireland. Reference to Ireland and quality sport horses is important in the website.

Current website is www.sorchapelletrow.com. One page in particular that I need is a "Sport Horses" page as well as a "References" page. Layout for each to be similar to this one - https://www.brimlowfields.net/en/sporthorses

Another website I like the feel of is www.velarocourse.com
Colour theme to be charcoal grey with elements of lighter grey and cream, as per logo. Charcoal grey to be somewhat transparent, otherwise it takes over too much. Cream colour is also to be subtle and not too beige.

Please note that Pelletrow is one word.

Please note there are new photographs with which to work if desired.

Sick

Target Market(s)

Upmarket clients seeking high quality coaching services and high quality show jumping horses

Number of Pages Required

2 page

Font styles to use
Serif
Sans Serif

Colors

Designer to choose only greyscale colors for use in the design.

Requirements
Must have
• A clean, simple, elegant look to the final design. OVerall theme colours must be subtle and include charcoal grey, light grey and cream. A design that will work well for mobile also. Please include only photographs provided or on the old website.
Nice to have
• artistically integrated photographs. use of the logo.
Should not have
• Anything fussy.

```html
<!DOCTYPE html>
<html lang="en">
<head>
<meta charset="utf-8">
<title>Pelletrow – Sport Horses &amp; Coaching</title>
<link rel="stylesheet" href="https://fonts.googleapis.com/css2?family=Playfair+Display:wght@400;700&family=Lora:wght@400&display=swap">
<style>
:root{
  --charcoal:#393939;
  --charcoal-deep:#2c2c2c;
  --tile:#4a4a4a;
  --tile-inner:#555;
  --gold:#c9b27c;
  --gold-soft:#a8956a;
  --cream:#eeeae0;
  --text:#d8d6d0;
  --line:#8a8066;
}
*{margin:0;padding:0;box-sizing:border-box}
html,body{width:1200px;height:4060px;overflow:hidden}
body{position:relative;background:var(--charcoal);color:var(--text);font-family:"Lora",serif}
.abs{position:absolute}
.serif{font-family:"Playfair Display",serif}
/* nav */
.nav{top:0;left:0;width:1200px;height:60px;z-index:3}
.brand{left:192px;top:12px;font-family:"Playfair Display",serif;font-size:24px;color:var(--cream);font-weight:400}
.menu{left:438px;top:22px;display:flex;gap:34px;font-size:11px;color:var(--cream)}
.menu span.active{color:var(--gold);border-bottom:1px solid var(--gold);padding-bottom:4px}
/* hero */
.hero{top:0;left:0;width:1200px;height:570px;background:linear-gradient(180deg,#262626 0%,#4d4d4d 40%,#5a5a5a 70%,#3a3a3a 100%)}
.hero-box{left:371px;top:170px;width:457px;height:205px;background:rgba(40,40,40,.75);border:1px solid var(--line);text-align:center;color:#fff}
.hero-box .small{font-family:"Playfair Display",serif;font-size:44px;margin-top:26px;line-height:1}
.hero-box .big{font-family:"Playfair Display",serif;font-weight:700;font-size:76px;line-height:1.05}
.dots{left:568px;top:400px;display:flex;gap:8px;align-items:center}
.dots i{display:block;width:6px;height:6px;border-radius:50%;background:#fff}
.dots i.on{width:12px;height:12px;border:2px solid #fff;background:transparent;position:relative}
/* titles */
.title{left:0;width:1200px;text-align:center;font-family:"Playfair Display",serif;font-size:40px;color:#fff;font-weight:400}
.title b{color:var(--gold);font-weight:400}
.rule{left:515px;width:170px;height:10px}
.btn{height:30px;width:120px;left:540px;text-align:center;line-height:30px;font-size:12px;color:#3a3326;
  background:linear-gradient(90deg,rgba(201,178,124,0),var(--gold) 25%,var(--gold) 75%,rgba(201,178,124,0))}
/* about */
.about-bg{top:570px;left:0;width:1200px;height:540px;background:linear-gradient(180deg,#3a3a3a,#363636)}
.about-text{left:256px;top:765px;width:688px;text-align:center;font-size:11.4px;line-height:17.5px;color:var(--text)}
.about-text p+p{margin-top:17px}
/* banner */
.banner{top:1112px;left:0;width:1200px;height:292px;background:linear-gradient(180deg,#4c4c52 0%,#5a4f47 45%,#3f3a36 100%)}
.banner h2{top:1212px;left:0;width:1200px;text-align:center;font-family:"Playfair Display",serif;font-size:36px;color:#fff;font-weight:400}
/* services */
.svc-photo{left:192px;top:1569px;width:207px;height:319px;border:1px solid var(--line)}
.svc-photo .img{position:absolute;left:10px;top:8px;width:178px;height:302px;background:linear-gradient(160deg,#b9b9b9,#6b6b6b 55%,#3d3d3d)}
.svc-photo .frame{position:absolute;left:20px;top:16px;width:185px;height:300px;border:1px solid var(--line)}
.tile{width:183px;height:139px;background:var(--tile)}
.tile .inner{position:absolute;left:12px;top:12px;right:12px;bottom:12px;border:1px solid var(--line);text-align:center;padding-top:42px}
.tile .name{font-family:"Playfair Display",serif;font-size:19px;color:var(--gold)}
.tile.current .inner{background:var(--tile-inner);border-color:#ddd}
.tile.current .name{color:#fff}
.tile svg{display:block;margin:8px auto 0}
/* horses */
.horse{width:395px;height:245px}
.horse .f1{position:absolute;left:0;top:0;width:360px;height:230px;border:1px solid var(--line)}
.horse .f2{position:absolute;left:35px;top:35px;width:360px;height:210px;border:1px solid var(--line)}
.horse .img{position:absolute;left:18px;top:18px;width:362px;height:210px}
.play{position:absolute;left:50%;top:50%;width:46px;height:46px;margin:-23px 0 0 -23px}
/* partners */
.partners{top:2586px;left:0;width:1200px;height:300px;background:linear-gradient(90deg,#4a4a4a,#5c5c5c 50%,#4e4e4e)}
.logo-row{top:2752px;left:190px;width:820px;display:flex;justify-content:space-between;align-items:center;font-family:"Playfair Display",serif;font-size:21px;color:var(--gold)}
.logo-row span{display:flex;align-items:center;gap:6px}
.logo-row span i{display:block;width:10px;height:10px;background:var(--gold)}
/* gallery */
.g{width:185px;height:184px}
.zoom{background:rgba(40,40,40,.85)}
.zoom .inner{position:absolute;left:12px;top:12px;right:12px;bottom:12px;border:1px solid var(--line);text-align:center;padding-top:52px;color:#ddd;font-size:12px}
/* contact */
.col-h{top:3740px;font-family:"Playfair Display",serif;font-size:24px;color:#fff}
.info{font-size:11px;color:var(--gold);display:flex;gap:10px;line-height:16px}
.field{border:1px solid #cfcfcf;font-size:10px;color:#ddd;padding:4px 8px}
.send{background:var(--gold);color:#3a3326;font-size:10px;text-align:center;line-height:23px}
.social{width:24px;height:24px;border:2px solid var(--gold);border-radius:3px}
.copy{top:4032px;left:0;width:1200px;text-align:center;font-size:10px;color:var(--gold)}
</style>
</head>
<body>

<!-- Hero -->
<div class="abs hero" role="img" aria-label="Black and white photograph of a show jumping rider in a helmet on a horse"></div>
<header class="abs nav">
  <div class="abs brand">Pelletrow</div>
  <nav class="abs menu"><span class="active">Home</span><span>About Us</span><span>Horses</span><span>Sponsors</span><span>Facilities &amp; Services</span><span>Gallery</span><span>Contact Us</span></nav>
</header>
<div class="abs hero-box"><div class="small">Welcome to</div><div class="big">Pelletrow</div></div>
<div class="abs dots"><i></i><i></i><i class="on"></i><i></i><i></i></div>

<!-- About -->
<div class="abs about-bg"></div>
<h2 class="abs title" style="top:645px">About <b>Us</b></h2>
<svg class="abs rule" style="top:712px" viewBox="0 0 170 10"><line x1="0" y1="5" x2="76" y2="5" stroke="#8a8066"/><line x1="94" y1="5" x2="170" y2="5" stroke="#8a8066"/><circle cx="85" cy="5" r="3.5" fill="#c9b27c"/></svg>
<div class="abs about-text">
  <p>Sorcha is an accomplished rider, sport horse producer and equestrian coach. Following the purchase of the seven-year-old gelding “Solstice” from Holland, at the age of just 16 Sorcha and he formed an exceptional partnership and successfully progressed through the ranks to the very top level of show jumping on a global scale. Over the next few years the partnership would make four European Championship team appearances for Ireland, win a Senior National Championship title (still being the youngest female ever to do so), achieve global success at CSI5* level and achieve the ultimate Irish rider’s dream of selection for the Irish Team competing in the Leinster Nations Trophy at the Leinster Horse Show, where Sorcha helped Ireland to finish in runner-up position.</p>
  <p>During this period, Sorcha was also pursuing her studies in Liffey College, but upon graduating with a degree in Electronic Engineering in 2010, she chose to pursue her passion of show jumping over an engineering career. This business entailed sourcing, training, competing and selling younger show jumping horses, as well as providing high-quality coaching, from her yard in Co. Kildare.</p>
</div>
<div class="abs btn" style="top:1013px">Read More</div>

<!-- Buy / sell banner -->
<div class="abs banner" role="img" aria-label="Photograph of a show jumping arena with a crowded grandstand"></div>
<h2 class="abs" style="top:1210px;left:0;width:1200px;text-align:center;font-family:'Playfair Display',serif;font-size:36px;color:#fff;font-weight:400">Do You Want To Buy Or Sell Horse?</h2>
<div class="abs btn" style="top:1305px">Contact Us</div>

<!-- Services -->
<h2 class="abs title" style="top:1452px">Our <b>Services</b></h2>
<svg class="abs rule" style="top:1519px" viewBox="0 0 170 10"><line x1="0" y1="5" x2="76" y2="5" stroke="#8a8066"/><line x1="94" y1="5" x2="170" y2="5" stroke="#8a8066"/><circle cx="85" cy="5" r="3.5" fill="#c9b27c"/></svg>
<div class="abs svc-photo"><div class="frame"></div><div class="img" role="img" aria-label="Black and white photograph of a rider standing beside her horse"></div></div>

<div class="abs tile" style="left:408px;top:1577px"><div class="inner"><div class="name">Facility</div><svg width="30" height="10" viewBox="0 0 30 10"><path d="M0 5H28M23 1l5 4-5 4" stroke="#c9b27c" fill="none"/></svg></div></div>
<div class="abs tile current" style="left:610px;top:1577px"><div class="inner"><div class="name">Coaching</div><svg width="30" height="10" viewBox="0 0 30 10"><path d="M0 5H28M23 1l5 4-5 4" stroke="#fff" fill="none"/></svg></div></div>
<div class="abs tile" style="left:812px;top:1577px"><div class="inner"><div class="name">Sales Agent</div><svg width="30" height="10" viewBox="0 0 30 10"><path d="M0 5H28M23 1l5 4-5 4" stroke="#c9b27c" fill="none"/></svg></div></div>
<div class="abs tile" style="left:408px;top:1736px"><div class="inner"><div class="name">Livery</div><svg width="30" height="10" viewBox="0 0 30 10"><path d="M0 5H28M23 1l5 4-5 4" stroke="#c9b27c" fill="none"/></svg></div></div>
<div class="abs tile" style="left:610px;top:1736px"><div class="inner"><div class="name">Schooling</div><svg width="30" height="10" viewBox="0 0 30 10"><path d="M0 5H28M23 1l5 4-5 4" stroke="#c9b27c" fill="none"/></svg></div></div>
<div class="abs tile" style="left:812px;top:1736px"><div class="inner"><div class="name">Consultancy</div><svg width="30" height="10" viewBox="0 0 30 10"><path d="M0 5H28M23 1l5 4-5 4" stroke="#c9b27c" fill="none"/></svg></div></div>
<div class="abs btn" style="top:1942px;width:170px;left:515px">Explore Services</div>

<!-- Horses -->
<h2 class="abs title" style="top:2041px">Our <b>Horses</b></h2>
<svg class="abs rule" style="top:2108px" viewBox="0 0 170 10"><line x1="0" y1="5" x2="76" y2="5" stroke="#8a8066"/><line x1="94" y1="5" x2="170" y2="5" stroke="#8a8066"/><circle cx="85" cy="5" r="3.5" fill="#c9b27c"/></svg>
<div class="abs horse" style="left:192px;top:2172px"><div class="f1"></div><div class="f2"></div>
  <div class="img" role="img" aria-label="Video still of a horse and rider clearing a jump under a blue sky" style="background:linear-gradient(180deg,#6d8fc4 0%,#9ab3d9 45%,#8a6a4a 70%,#5f7d3c 100%)">
  <svg class="play" viewBox="0 0 46 46"><circle cx="23" cy="23" r="21" fill="rgba(255,255,255,.85)"/><circle cx="23" cy="23" r="14" fill="none" stroke="#333" stroke-width="2"/><path d="M20 17l9 6-9 6z" fill="#333"/></svg></div></div>
<div class="abs horse" style="left:610px;top:2172px"><div class="f1"></div><div class="f2"></div>
  <div class="img" role="img" aria-label="Video still of a rider standing with her bay horse" style="background:linear-gradient(135deg,#4a7a3a 0%,#6b4a30 40%,#d8d8d8 75%,#4f7c3f 100%)">
  <svg class="play" viewBox="0 0 46 46"><circle cx="23" cy="23" r="21" fill="rgba(255,255,255,.85)"/><circle cx="23" cy="23" r="14" fill="none" stroke="#333" stroke-width="2"/><path d="M20 17l9 6-9 6z" fill="#333"/></svg></div></div>
<div class="abs btn" style="top:2486px">View All</div>

<!-- Partners -->
<div class="abs partners" role="img" aria-label="Photograph of a rider at an international competition with a results scoreboard"></div>
<h2 class="abs title" style="top:2621px">Our <b>Partners</b></h2>
<svg class="abs rule" style="top:2688px" viewBox="0 0 170 10"><line x1="0" y1="5" x2="76" y2="5" stroke="#8a8066"/><line x1="94" y1="5" x2="170" y2="5" stroke="#8a8066"/><circle cx="85" cy="5" r="3.5" fill="#c9b27c"/></svg>
<div class="abs logo-row"><span>Ardmore Tack</span><span>Corrib Feeds</span><span>Rivermead</span><span><i></i>Stepwell</span><span>Tidewell Equine</span></div>
<svg class="abs" style="left:555px;top:2838px" width="90" height="18" viewBox="0 0 90 18"><path d="M36 9H2M8 3L2 9l6 6" stroke="#fff" stroke-width="2" fill="none"/><path d="M54 9H88M82 3l6 6-6 6" stroke="#fff" stroke-width="2" fill="none"/></svg>

<!-- Gallery -->
<h2 class="abs title" style="top:2958px;left:-10px">Our <b>Gallery</b></h2>
<svg class="abs rule" style="top:3025px;left:505px" viewBox="0 0 170 10"><line x1="0" y1="5" x2="76" y2="5" stroke="#8a8066"/><line x1="94" y1="5" x2="170" y2="5" stroke="#8a8066"/><circle cx="85" cy="5" r="3.5" fill="#c9b27c"/></svg>
<div class="abs g" style="left:192px;top:3099px;background:linear-gradient(180deg,#5d8f3f,#e8e8e8 55%,#b03030)" role="img" aria-label="Horse jumping in front of a white marquee"></div>
<div class="abs g" style="left:396px;top:3099px;background:linear-gradient(180deg,#3a5aa0,#d9c24a 60%,#2f4f8a)" role="img" aria-label="Horse jumping a fence with sponsor banners"></div>
<div class="abs g" style="left:599px;top:3099px;background:linear-gradient(180deg,#5a6a7a,#2f4a3a 55%,#dedede)" role="img" aria-label="Rider in a green team jacket walking the course"></div>
<div class="abs g" style="left:801px;top:3099px;background:linear-gradient(135deg,#4d7a3a,#6a4530 50%,#dcdcdc)" role="img" aria-label="Rider beside a bay horse outdoors"></div>
<div class="abs g" style="left:192px;top:3302px;background:linear-gradient(135deg,#4a7a3a,#5a3a26 45%,#e5e5e5)" role="img" aria-label="Rider with her horse at a show"></div>
<div class="abs g zoom" style="left:396px;top:3302px"><div class="inner"><svg width="30" height="30" viewBox="0 0 30 30"><circle cx="13" cy="13" r="10" fill="none" stroke="#ddd" stroke-width="1.5"/><path d="M20 20l8 8M13 8v10M8 13h10" stroke="#ddd" stroke-width="1.5"/></svg><div style="margin-top:6px">Click For Zoom</div></div></div>
<div class="abs g" style="left:599px;top:3302px;background:linear-gradient(180deg,#7a9a6a,#4e7a3a 50%,#b8a890)" role="img" aria-label="Horse and rider schooling in a sand arena"></div>
<div class="abs g" style="left:801px;top:3302px;background:linear-gradient(180deg,#8a8a7a,#6a4a30 50%,#4f8a36)" role="img" aria-label="Horse jumping on a grass arena"></div>
<div class="abs btn" style="top:3530px;left:530px">View All</div>

<!-- Contact -->
<h2 class="abs title" style="top:3616px">Contact <b>Us</b></h2>
<svg class="abs rule" style="top:3683px" viewBox="0 0 170 10"><line x1="0" y1="5" x2="76" y2="5" stroke="#8a8066"/><line x1="94" y1="5" x2="170" y2="5" stroke="#8a8066"/><circle cx="85" cy="5" r="3.5" fill="#c9b27c"/></svg>

<div class="abs col-h" style="left:200px">Address</div>
<div class="abs info" style="left:200px;top:3808px"><svg width="10" height="14" viewBox="0 0 10 14"><path d="M5 0a5 5 0 0 1 5 5c0 4-5 9-5 9S0 9 0 5a5 5 0 0 1 5-5z" fill="#c9b27c"/><circle cx="5" cy="5" r="2" fill="#393939"/></svg><div>Ballinure Rathmore<br>Co. Kildare Ireland</div></div>
<div class="abs info" style="left:200px;top:3865px"><svg width="12" height="12" viewBox="0 0 12 12"><path d="M2 0l3 3-1.5 2a7 7 0 0 0 3.5 3.5L9 7l3 3-2 2C5 12 0 7 0 2z" fill="#c9b27c"/></svg><div>+353 87 000 4821</div></div>
<div class="abs info" style="left:200px;top:3906px"><svg width="12" height="10" viewBox="0 0 12 10"><rect width="12" height="10" fill="#c9b27c"/><path d="M0 0l6 5 6-5" stroke="#393939" fill="none"/></svg><div>sorcha@sorchapelletrow.com</div></div>

<div class="abs col-h" style="left:483px">Send Message</div>
<div class="abs field" style="left:483px;top:3805px;width:167px;height:24px">Your Email</div>
<div class="abs field" style="left:483px;top:3843px;width:167px;height:24px">Subject</div>
<div class="abs field" style="left:483px;top:3880px;width:167px;height:56px">Your Message</div>
<div class="abs send" style="left:483px;top:3957px;width:64px;height:23px">Send</div>

<div class="abs col-h" style="left:744px">Subscribe Newsletter</div>
<div class="abs field" style="left:744px;top:3805px;width:192px;height:24px">Your Email</div>
<div class="abs send" style="left:936px;top:3805px;width:61px;height:24px">Submit</div>
<div class="abs social" style="left:746px;top:3874px" aria-label="Social link"></div>
<div class="abs social" style="left:802px;top:3874px" aria-label="Social link"></div>
<div class="abs social" style="left:858px;top:3874px" aria-label="Social link"></div>

<div class="abs copy">Copyright © 2019 All rights reserved.</div>
</body>
</html>
```